ROVA Pty Ltd Business Card

Looking for a simple yet eye-catching double-sided business card design using my company logo on one side and contact details on the other.

Target Market(s)

Government

Industry/Entity Type

Communication Systems Engineering

Contact Information for Business Card

ROVA Pty Ltd

Requirements
Nice to have
• Would be great to have a QR code so details can be scanned into contacts

```html
<!DOCTYPE html>
<html lang="en">
<head>
<meta charset="utf-8">
<title>ROVA Pty Ltd — Business Card</title>
<link href="https://fonts.googleapis.com/css2?family=Raleway:wght@400;600;700&family=Lato:wght@400&display=swap" rel="stylesheet">
<style>
  :root {
    --page-bg: #eef1f4;
    --card-white: #ffffff;
    --panel-dark: #2d2d2d;
    --brand-slate: #37424a;
    --ink-light: #ffffff;
    --ink-muted: #d9d9d9;
  }
  * { box-sizing: border-box; margin: 0; padding: 0; }
  html, body { width: 1200px; height: 1200px; overflow: hidden; }
  body {
    background: var(--page-bg);
    position: relative;
    font-family: "Raleway", sans-serif;
  }
  .card {
    position: absolute;
    left: 173px;
    width: 854px;
    height: 512px;
    background: var(--card-white);
    overflow: hidden;
  }
  .card--front { top: 70px; }
  .card--back { top: 624px; }

  /* Front */
  .contact-panel {
    position: absolute;
    left: 427px; top: 0;
    width: 427px; height: 100%;
    background: var(--panel-dark);
  }
  .icon-tab {
    position: absolute;
    left: 382px;
    width: 90px; height: 90px;
    border-radius: 50%;
    background: var(--card-white);
    display: flex; align-items: center; justify-content: center;
  }
  .icon-tab svg { width: 40px; height: 40px; fill: var(--panel-dark); }
  .icon-tab--phone { top: 203px; }
  .icon-tab--web { top: 281px; }
  .icon-tab--home { top: 365px; }

  .front-brand {
    position: absolute;
    left: 0; top: 0;
    width: 427px; height: 100%;
    display: flex; align-items: center; justify-content: center;
  }
  .brand-name {
    font-family: "Raleway", sans-serif;
    font-weight: 700;
    color: var(--brand-slate);
    letter-spacing: 0.06em;
    line-height: 1;
  }
  .front-brand .brand-name { font-size: 68px; margin-left: 14px; }

  .person {
    position: absolute;
    left: 441px; top: 52px;
    color: var(--ink-light);
  }
  .person-name {
    font-size: 38px;
    font-weight: 400;
    letter-spacing: 0.01em;
  }
  .person-name strong { font-weight: 700; }
  .person-role {
    font-size: 23px;
    color: var(--ink-muted);
    margin: 4px 0 0 46px;
  }

  .contact-line {
    position: absolute;
    left: 499px;
    color: var(--ink-light);
    font-family: "Lato", sans-serif;
    line-height: 1.12;
  }
  .contact-line--phone { top: 222px; font-size: 23px; }
  .contact-line--web { top: 304px; font-size: 23px; }
  .contact-line--address { top: 392px; font-size: 18px; line-height: 1.1; }

  /* Back */
  .back-brand {
    position: absolute;
    inset: 0;
    display: flex; align-items: center; justify-content: center;
    gap: 50px;
  }
  .brand-dot {
    width: 150px; height: 150px;
    border-radius: 50%;
    background: var(--brand-slate);
  }
  .back-brand .brand-name { font-size: 96px; }
  .back-strip {
    position: absolute;
    left: 0; bottom: 0;
    width: 100%; height: 11px;
    background: var(--panel-dark);
  }
</style>
</head>
<body>

<section class="card card--front" aria-label="Business card front">
  <div class="front-brand">
    <span class="brand-name">ROVA</span>
  </div>
  <div class="contact-panel"></div>

  <div class="icon-tab icon-tab--phone">
    <svg viewBox="0 0 24 24" aria-hidden="true">
      <path d="M3 8c0-2 2-3 9-3s9 1 9 3v1.5h-4.5V8c-1-.6-2.6-.8-4.5-.8S8.5 7.4 7.5 8v1.5H3z"/>
      <path d="M6 11h12l2 7v2H4v-2z"/>
      <circle cx="12" cy="15.5" r="2.2" fill="#fff"/>
    </svg>
  </div>
  <div class="icon-tab icon-tab--web">
    <svg viewBox="0 0 24 24" aria-hidden="true">
      <path d="M12 2a10 10 0 1 0 0 20 10 10 0 0 0 0-20zm0 1.8c1 0 2.3 2 2.8 5.2H9.2C9.7 5.8 11 3.8 12 3.8zM8.9 4.6C8.2 5.8 7.7 7.3 7.4 9H4.8a8.2 8.2 0 0 1 4.1-4.4zm6.2 0A8.2 8.2 0 0 1 19.2 9h-2.6c-.3-1.7-.8-3.2-1.5-4.4zM4.2 10.8h3v2.4h-3a8 8 0 0 1 0-2.4zm4.8 0h6v2.4H9zm7.8 0h3a8 8 0 0 1 0 2.4h-3zM4.8 15h2.6c.3 1.7.8 3.2 1.5 4.4A8.2 8.2 0 0 1 4.8 15zm4.4 0h5.6c-.5 3.2-1.8 5.2-2.8 5.2S9.7 18.2 9.2 15zm7.4 0h2.6a8.2 8.2 0 0 1-4.1 4.4c.7-1.2 1.2-2.7 1.5-4.4z"/>
    </svg>
  </div>
  <div class="icon-tab icon-tab--home">
    <svg viewBox="0 0 24 24" aria-hidden="true">
      <path d="M12 3 1.5 12.2l1.3 1.4L12 5.6l9.2 8 1.3-1.4z"/>
      <path d="M5 13.2 12 7.2l7 6V21h-5v-5h-4v5H5z"/>
    </svg>
  </div>

  <div class="person">
    <h1 class="person-name"><strong>DANIEL</strong> HARPER</h1>
    <p class="person-role">Solution Manager</p>
  </div>

  <p class="contact-line contact-line--phone">+000 12345 6789<br>+000 12345 6789</p>
  <p class="contact-line contact-line--web">www.rova.com.au<br>admin@rova.com.au</p>
  <p class="contact-line contact-line--address">42 Harbour Lane Milford<br>NSW 2099 Australia</p>
</section>

<section class="card card--back" aria-label="Business card back">
  <div class="back-brand">
    <span class="brand-dot"></span>
    <span class="brand-name">ROVA</span>
  </div>
  <div class="back-strip"></div>
</section>

</body>
</html>
```